Fun conversation piece for the home depicting the history of the ownership (title) and more!

We need some ideas for a framed display to be hung in a home for a new company I started called Wanderlane Keepsakes, LLC. We will create framed (or unframed canvass) wall displays depicting the History of the Home (title transfers) with some interesting background on the subdivision the home is located. This will be a conversation piece. Use color if you feel that works best. I am envisioning perhaps the writing to be in old English or old Spanish font to reflect the history of Florida where I am located. I am wanting to incorporate perhaps a picture of the home converted into sketch as a background to the "history". Or we could skip that and use the vegetation (trees) native to the area for a background. I am going to attach something I found online as a sample but I am open to ideas. The sample is a little formal for what I am trying to do. I may sell these framed or as unframed canvass pictures which might need to be a bit more contemporary. I also need a logo if you have any ideas. WK in some form of old English style perhaps? The document attached labeled "Marlowbrook" is an example of the content I will be creating for the picture.

I misspelled "States" in one of the paragraphs. Can you correct that for me? United States. Not "sates". My bad.

Logo Text

Wanderlane Keepsakes (or WK). Surprise me.

```html
<!DOCTYPE html>
<html lang="en">
<head>
<meta charset="utf-8">
<title>Marlowbrook – History Home</title>
<link href="https://fonts.googleapis.com/css2?family=Rye&family=Crimson+Pro:ital,wght@0,600;1,500&family=Pinyon+Script&display=swap" rel="stylesheet">
<style>
  :root {
    --ink: #111111;
    --title-ink: #4a4430;
    --paper: #ffffff;
    --sketch-green: #9fae8a;
    --sketch-light: #e3e9da;
    --ornament: #2a2a2a;
  }
  * { box-sizing: border-box; margin: 0; padding: 0; }
  html, body { width: 1019px; height: 1200px; overflow: hidden; background: var(--paper); }
  .canvas { position: relative; width: 1019px; height: 1200px; }
  .certificate {
    position: absolute; left: 88px; top: 20px; width: 842px; height: 1160px;
    border: 3px solid var(--ink); background: var(--paper);
  }
  .certificate::before {
    content: ""; position: absolute; inset: 6px; border: 1.5px solid var(--ink);
  }
  .corner-ornament {
    position: absolute; width: 80px; height: 80px;
    background: radial-gradient(circle, transparent 40%, rgba(0,0,0,.25) 42%, transparent 60%);
  }
  .corner-ornament.tl { left: 2px; top: 2px; }
  .corner-ornament.tr { right: 2px; top: 2px; }
  .corner-ornament.bl { left: 2px; bottom: 2px; }
  .corner-ornament.br { right: 2px; bottom: 2px; }
  .wave-band { position: absolute; background: #cfcfcf; }
  .wave-band.top { left: 117px; top: 24px; width: 612px; height: 6px; }
  .wave-band.bottom { left: 117px; top: 1123px; width: 612px; height: 6px; }
  .wave-band.left { left: 18px; top: 118px; width: 6px; height: 952px; }
  .wave-band.right { right: 18px; top: 118px; width: 6px; height: 952px; }
  .home-sketch {
    position: absolute; left: 149px; top: 286px; width: 584px; height: 344px;
    background: radial-gradient(ellipse at 50% 40%, var(--sketch-green) 0%, var(--sketch-light) 55%, rgba(255,255,255,0) 75%);
    opacity: .75;
  }
  .neighborhood-title {
    position: absolute; left: 0; right: 0; top: 96px; text-align: center;
    font-family: "Rye", serif; font-size: 56px; color: var(--title-ink); letter-spacing: 2px;
  }
  .history-body {
    position: absolute; left: 72px; top: 198px; width: 696px;
    font-family: "Crimson Pro", serif; font-style: italic; font-weight: 500;
    font-size: 15.5px; line-height: 21.6px; color: var(--ink); text-align: justify;
  }
  .history-body p + p { margin-top: 21.6px; }
  .section-title {
    position: absolute; left: 0; right: 0; top: 650px; text-align: center;
    font-family: "Rye", serif; font-size: 44px; color: var(--title-ink);
  }
  .ownership-chain {
    position: absolute; left: 77px; top: 751px; width: 700px; border-collapse: collapse;
    font-family: "Crimson Pro", serif; font-style: italic; font-weight: 500;
    font-size: 15.5px; line-height: 21.6px; color: var(--ink);
  }
  .ownership-chain td { padding: 0; vertical-align: top; }
  .ownership-chain .date { width: 338px; }
  .presented-by {
    position: absolute; left: 0; right: 0; top: 952px; text-align: center;
    font-family: "Pinyon Script", cursive; font-size: 40px; color: var(--ink);
  }
  .presenter {
    position: absolute; left: 0; right: 0; top: 1014px; text-align: center;
    font-family: "Crimson Pro", serif; font-weight: 600; font-size: 30px; color: var(--ink);
  }
</style>
</head>
<body>
<div class="canvas">
  <div class="certificate">
    <div class="corner-ornament tl" role="img" aria-label="Interlaced ring corner ornament"></div>
    <div class="corner-ornament tr" role="img" aria-label="Interlaced ring corner ornament"></div>
    <div class="corner-ornament bl" role="img" aria-label="Interlaced ring corner ornament"></div>
    <div class="corner-ornament br" role="img" aria-label="Interlaced ring corner ornament"></div>
    <div class="wave-band top" role="img" aria-label="Wavy border ornament"></div>
    <div class="wave-band bottom" role="img" aria-label="Wavy border ornament"></div>
    <div class="wave-band left" role="img" aria-label="Wavy border ornament"></div>
    <div class="wave-band right" role="img" aria-label="Wavy border ornament"></div>

    <div class="home-sketch" role="img" aria-label="Faded green sketch of the house beneath tall oak trees"></div>

    <h1 class="neighborhood-title">MARLOWBROOK</h1>

    <div class="history-body">
      <p>Marlowbrook is a neighborhood in the City of Pensacola. Located east of Cedar Hollow, Marlowbrook is bordered by 9th Avenue to the west and 12th Avenue and Miller's Creek to the east. Initially developed in 1954, an addition was added in 1956. It is located in a beautiful area of America's 1st Settlement (1559), Pensacola, Florida encompassed with towering pine trees and breathtaking heritage oaks.</p>
      <p>The land comprising Marlowbrook was originally owned by Tomás Bellaver under a Spanish Land Grant and affirmed by President Elias Thornbury on September 7, 1835. Spain relinquished Florida to the United States in 1819 under the Adams-Onis Treaty and lands previously granted to settlers prior thereto were honored if claims were filed and approved by the United States government.</p>
      <p>Through the years, the land changed hands many times but was eventually developed into the Marlowbrook subdivision in 1954, by Warren Ashby, President of Marlowbrook, Inc. The subdivision contains 63 lots with a beautiful, oak-filled park located just off of Hollis Street. Built in 1957 and containing approximately 2606 square feet of living, garage and patio space, the home located at 418 Larkspur Street is a trip back in time to when houses were carefully planned catering to modern sensibilities, neither too big nor too small, neither too formal nor too casual.</p>
    </div>

    <h2 class="section-title">History Home</h2>

    <table class="ownership-chain">
      <tr><td class="date">September 9, 1835</td><td>Tomás Bellaver, Spanish Land Grant</td></tr>
      <tr><td class="date">April 27, 1954</td><td>Marlowbrook Plat approved by Escambia County</td></tr>
      <tr><td class="date">April 29, 1957</td><td>Warren Ashby, III and Nora W. Ashby</td></tr>
      <tr><td class="date">September 20, 1960</td><td>Clara Mae Dunning (Harwell)</td></tr>
      <tr><td class="date">February 11, 1966</td><td>Walter J. Pruitt and Helen R. Pruitt</td></tr>
      <tr><td class="date">January 20, 1995</td><td>Daniel R. Corbin</td></tr>
      <tr><td class="date">September 1, 2020</td><td>Daniel R. Corbin and Martin Ellery Vance</td></tr>
    </table>

    <p class="presented-by">Presented By</p>
    <p class="presenter">WANDERLANE KEEPSAKES, LLC</p>
  </div>
</div>
</body>
</html>
```